Varnell Contracting In need of monthly newsletter

We need a monthly newsletter to promote our monthly special of Mulch Installation.

Please change wording to fit what you feel is professional and effective.

Our regular price to install Mulch is $169/Yard installed/Delivered

We would like to run a promotion of $125/Yard Installed & Delivered

Compare us to others $135/Yard Delivered only from some other suppliers

Also list somewhere on the newsletter :
- Delivery of soils, stone, wood also available
- Check out our website
- an emphasis on quality

The Fine Print
* Some Conditions apply
Mulches included in sale Onyx Velvet, Chocolate Brown, Auburn Red, Natural, Hemlock, Gold, Shredded Pine. Some site conditions may incur extra cost. minimum 3 Yards for sale price to be in effect, HST extra on all prices listed,

CHECK OUR WEBSITE FOR SOME IMAGES AND MORE INFORMATION....

ASK ANYTHING YOU WANT VIA Draft Plaza
Updates

Types of Mulch have changed Slightly in the "Fine Print"

Classic Cedar, Black Cedar, Red Cedar, Chocolate brown, Pine Bark, Natural Shredded Pine, Hemlock, Utility Style.

We will also be submitting pictures of the mulch HOWEVER you might need to crop or alter these images to make them work for our newsletter.

Project Deadline Extended
Reason: We have not yet found a design we think is Straight to the point. Simple and with our theme.

```html
<!DOCTYPE html>
<html lang="en">
<head>
<meta charset="utf-8">
<title>Varnell Contracting – Mulch Install Sale</title>
<link href="https://fonts.googleapis.com/css2?family=Anton&family=Archivo+Black&family=Arimo:wght@400;700&family=Oswald:wght@600&display=swap" rel="stylesheet">
<style>
  :root{
    --bg:#3c3c3c;
    --lime:#88c641;
    --forest:#1d5a2c;
    --forest-dark:#174d25;
    --ink:#161616;
    --pale:#f4f9ec;
    --mint:#b9dd8a;
    --grey:#6d6d6d;
    --white:#ffffff;
  }
  *{margin:0;padding:0;box-sizing:border-box}
  html,body{width:978px;height:1200px;overflow:hidden;background:var(--bg)}
  .canvas{position:relative;width:978px;height:1200px;background:var(--bg);font-family:"Arimo",Arial,sans-serif}
  .flyer{position:absolute;left:55px;top:42px;width:867px;height:1115px;overflow:hidden;
    background:linear-gradient(180deg,#ffffff 0%,var(--pale) 45%,var(--mint) 100%);
    box-shadow:0 0 18px rgba(0,0,0,.55)}
  .abs{position:absolute}

  .hero-photo{left:0;top:0;width:452px;height:357px;
    background:
      radial-gradient(ellipse 150px 70px at 110px 30px,rgba(236,238,234,.95),rgba(236,238,234,0) 100%),
      radial-gradient(ellipse 200px 120px at 40px 330px,rgba(30,24,18,.95),rgba(30,24,18,0) 100%),
      radial-gradient(ellipse 190px 60px at 170px 220px,rgba(170,200,120,.9),rgba(170,200,120,0) 100%),
      radial-gradient(ellipse 170px 120px at 350px 300px,rgba(118,168,66,.95),rgba(118,168,66,0) 100%),
      radial-gradient(ellipse 70px 40px at 390px 190px,rgba(60,48,34,.9),rgba(60,48,34,0) 100%),
      linear-gradient(180deg,#6f7b62 0%,#2f4a24 30%,#4f7e34 55%,#6a9e45 80%,#3a3224 100%)}

  .headline{left:452px;top:0;width:415px;height:357px;background:var(--lime);color:var(--ink);text-align:center}
  .headline .line{position:absolute;left:0;right:0;line-height:1;transform-origin:center top}
  .headline .mulch{top:36px;font-family:"Archivo Black",sans-serif;font-size:78px;letter-spacing:1px}
  .headline .install{top:112px;font-family:"Anton",sans-serif;font-size:54px;transform:scaleX(1.13)}
  .headline .price{top:178px;font-family:"Anton",sans-serif;font-size:76px;transform:scaleX(1.2)}
  .headline .price small{font-size:56px}
  .headline .delivered{top:266px;font-family:"Anton",sans-serif;font-size:32px;transform:scaleX(1.1)}
  .headline .compare{top:310px;font-size:12.5px;font-weight:700;line-height:16px}

  .rule{left:0;width:867px;background:var(--forest)}
  .swatch{top:366px;height:150px}
  .collage{left:397px;top:482px;width:414px;height:342px;background:var(--white);transform:rotate(1.6deg);
    box-shadow:0 12px 16px rgba(0,0,0,.45)}
  .collage .shot{position:absolute}

  .list-block{left:61px;top:543px;color:var(--ink)}
  .list-block h2{font-family:"Archivo Black",sans-serif;font-size:20px;line-height:27px;letter-spacing:.8px;font-weight:400}
  .list-block ul{list-style:none;margin-top:1px}
  .list-block li{font-size:21px;line-height:27.7px}
  .list-block li::before{content:"• "}
  .extras{left:61px;top:835px;color:var(--forest);font-size:18.5px;font-weight:700;line-height:24px}
  .brand{left:44px;top:905px;display:flex;align-items:center;gap:14px}
  .brand .dot{width:54px;height:54px;border-radius:50%;background:var(--forest)}
  .brand .name{font-family:"Arimo",sans-serif;font-weight:700;color:var(--grey);font-size:24px;line-height:27px;letter-spacing:2px}
  .banner{left:401px;top:854px;width:466px;height:34px;background:var(--forest);color:var(--white);
    font-family:"Oswald",sans-serif;font-weight:600;font-size:18.5px;line-height:34px;padding-left:38px}
  .banner-fold{left:401px;top:888px}
  .services{left:434px;top:903px;width:433px;height:89px;background:var(--white);font-size:12.5px;line-height:18px;color:var(--ink);padding:6px 0 0 22px;display:flex;gap:26px}
  .services h3{color:var(--forest);font-size:14.5px;font-weight:700;line-height:18px}
  .services ul{list-style:none}
  .services li::before{content:"• "}
  .fineprint{left:28px;top:1033px;font-size:10px;color:var(--ink)}
  .badge{top:1009px;height:38px;border-radius:3px}
  .footer{left:0;top:1054px;width:867px;height:61px;background:var(--forest-dark);color:var(--white);
    text-align:center;font-size:16px;line-height:48px}
  .footer .phone{font-size:22px;font-weight:700;letter-spacing:.5px}
</style>
</head>
<body>
<div class="canvas">
  <article class="flyer">
    <div class="abs hero-photo" role="img" aria-label="Garden bed freshly mulched with hostas, a wheelbarrow and shovel on the lawn"></div>

    <header class="abs headline">
      <div class="line mulch">MULCH</div>
      <div class="line install">INSTALL SALE</div>
      <div class="line price">$125<small>/Yard</small></div>
      <div class="line delivered">Installed &amp; Delivered*</div>
      <div class="line compare">Our Regular Price $169/Yard.<br>Compare to others&nbsp; $135/Yard Delivered</div>
    </header>

    <div class="abs rule" style="top:357px;height:9px"></div>

    <div class="abs swatch" style="left:0;width:228px;background:radial-gradient(ellipse 80px 55px at 112px 90px,#3a2518 0%,#4a3322 45%,rgba(74,51,34,0) 100%),radial-gradient(ellipse 60px 50px at 200px 120px,#5f9a3e,rgba(95,154,62,0)),linear-gradient(180deg,#7fa9d2 0%,#6b98c4 60%,#4f7fae 100%)" role="img" aria-label="Hands holding a pile of dark mulch"></div>
    <div class="abs swatch" style="left:228px;width:124px;background:radial-gradient(circle at 30% 30%,#b59876,rgba(181,152,118,0) 60%),radial-gradient(circle at 70% 75%,#4e3a28,rgba(78,58,40,0) 60%),#826749" role="img" aria-label="Natural shredded pine mulch"></div>
    <div class="abs swatch" style="left:352px;width:124px;background:radial-gradient(circle at 40% 40%,#4b3023,rgba(75,48,35,0) 60%),radial-gradient(circle at 75% 80%,#1a100b,rgba(26,16,11,0) 60%),#2e1d15" role="img" aria-label="Dark chocolate brown mulch"></div>
    <div class="abs swatch" style="left:476px;width:125px;background:radial-gradient(circle at 35% 35%,#eaa45c,rgba(234,164,92,0) 60%),radial-gradient(circle at 70% 80%,#a94f18,rgba(169,79,24,0) 60%),#cf7534" role="img" aria-label="Classic cedar mulch"></div>
    <div class="abs swatch" style="left:601px;width:124px;background:radial-gradient(circle at 35% 35%,#a48579,rgba(164,133,121,0) 60%),radial-gradient(circle at 70% 80%,#533832,rgba(83,56,50,0) 60%),#7b5d54" role="img" aria-label="Hemlock mulch"></div>
    <div class="abs swatch" style="left:725px;width:142px;background:radial-gradient(circle at 35% 35%,#ec8a8c,rgba(236,138,140,0) 60%),radial-gradient(circle at 70% 80%,#a8353b,rgba(168,53,59,0) 60%),#d35a5f" role="img" aria-label="Red cedar mulch"></div>

    <div class="abs rule" style="top:516px;height:7px"></div>

    <section class="abs list-block">
      <h2>MULCHES<br>INCLUDED IN SALE</h2>
      <ul>
        <li>Classic Cedar</li>
        <li>Black Cedar</li>
        <li>Red Cedar</li>
        <li>Chocolate brown</li>
        <li>Pine Bark</li>
        <li>Natural Shredded Pine</li>
        <li>Hemlock</li>
        <li>Utility Style</li>
      </ul>
    </section>

    <div class="abs extras">Delivery of soils, stone, wood<br>also available</div>

    <figure class="abs collage">
      <div class="shot" style="left:8px;top:8px;width:192px;height:196px;background:radial-gradient(ellipse 30px 120px at 70px 60px,#8d8576,rgba(141,133,118,0)),radial-gradient(ellipse 80px 50px at 150px 150px,#8a5b42,rgba(138,91,66,0)),linear-gradient(170deg,#5a3b28 0%,#3d271b 55%,#5b3c29 100%)" role="img" aria-label="Hand spreading mulch around a tree trunk"></div>
      <div class="shot" style="left:8px;top:206px;width:190px;height:128px;background:radial-gradient(ellipse 50px 30px at 150px 70px,#e58ad0,rgba(229,138,208,0)),radial-gradient(ellipse 120px 40px at 80px 50px,#2f6a2b,rgba(47,106,43,0)),linear-gradient(170deg,#a4a49c 0%,#6d6e66 30%,#2b2018 70%,#8b8a84 100%)" role="img" aria-label="Mulched front bed with shrubs and pink flowers"></div>
      <div class="shot" style="left:202px;top:8px;width:204px;height:326px;background:radial-gradient(ellipse 80px 200px at 150px 230px,#3a2519,rgba(58,37,25,0)),radial-gradient(ellipse 40px 90px at 120px 120px,#d9a742,rgba(217,167,66,0)),radial-gradient(ellipse 60px 200px at 20px 230px,#84c44a,rgba(132,196,74,0)),linear-gradient(180deg,#cdd3cc 0%,#9aa59a 12%,#3e6a2c 22%,#5d8d3a 40%,#3c2a1e 70%,#2f5a26 100%)" role="img" aria-label="Curved mulch bed with flowers beside a lawn"></div>
    </figure>

    <div class="abs brand">
      <span class="dot"></span>
      <span class="name">VARNELL<br>CONTRACTING<br>GROUP</span>
    </div>

    <div class="abs banner">Check Out Our Website An Emphasis On Quality</div>
    <svg class="abs banner-fold" width="9" height="10" viewBox="0 0 9 10"><polygon points="0,0 9,0 9,10" fill="#174d25"/></svg>

    <section class="abs services">
      <div>
        <h3>Other Services:</h3>
        <ul>
          <li>Landscape Management</li>
          <li>Snow &amp; Ice Management</li>
          <li>Parking Area Management</li>
        </ul>
      </div>
      <ul>
        <li>Irrigation Systems</li>
        <li>Landscape Design &amp; bould</li>
        <li>Trucking &amp; Roll Off Service</li>
        <li>Complete Building Maintenance</li>
      </ul>
    </section>

    <p class="abs fineprint">*Some site conditions may incur extra cost. Minimum 3 Yards for sale price to be in effect, HST extra on all prices listed.</p>

    <div class="abs badge" style="left:616px;width:96px;background:#1f4e79"></div>
    <div class="abs badge" style="left:720px;width:66px;background:#ffffff;border:2px solid #1f3f7a"></div>
    <div class="abs badge" style="left:792px;width:57px;background:#1b2f5e"></div>

    <footer class="abs footer">
      <span class="phone">555.204.7719</span> | info@varnellcontracting.com | www.varnellcontracting.com
    </footer>
  </article>
</div>
</body>
</html>
```